THE NAME OF THE COMPANY IS: VERDANT HOLLOWS. Services including: Excavation , Custom Property Designs, Sustainable Vegetable Gardens, Beautiful Floriculture. Licensed Contractor with 35 years experience. I am looking for 4 simple Icons: One a tractor, signifying the Excavation work, one a pencil and paper or ruler or something to signify Custom Designs, one a vegetable and one a flower. Similar Icons to the Moss Harbor Logos (attached). The Icons will all be simple but easily identifiable. All of them should look in the same style. I am thinking about a color screen of various olive toned greens. See PMS color chart attached.Probably a white reverse in green tone squares. I'd be interested in different layouts of a business card which will translate to signs and truck door magnets for a full sized truck. It'd also need it to translate to stationary and give away items.

Target Market(s)

The target market is a homeowner with disposable inclome to afford a high end Landscape Artist.

Industry/Entity Type

Business

Contact Information for Business Card

Verdant Hollows
Excavation, Custom Designs, Sustainable Gardens, Floriculture
Howard Pellin
Contractor
Ca. Lic. # C27-591046
PO Box 208716 Carlsbad, Ca 92013
760-382-9174

Colors
acd036
33b7a4

Requirements
Must have
• The company name VERDANT HOLLOWS needs to be prominent with the tag line: Excavation, Custom Property Designs, Sustainable Gardens and Floraculture being centered underneath the name. Be creative with the card color and use different shades of the greens I provided for the icons.

```html
<!DOCTYPE html>
<html lang="en">
<head>
<meta charset="utf-8">
<title>Verdant Hollows — Business Card</title>
<link href="https://fonts.googleapis.com/css2?family=Open+Sans:wght@400;600;700&display=swap" rel="stylesheet">
<style>
  :root {
    --backdrop: #ecebe6;
    --card-light: #e8ecdc;
    --card-mid: #d7ddc5;
    --card-edge: #c9d0b5;
    --tile: #8e9381;
    --ink: #989c89;
    --ink-strong: #8a8e7c;
    --band: #8b8f7d;
    --band-text: #f2f3ec;
  }
  * { margin: 0; padding: 0; box-sizing: border-box; }
  html, body { width: 1200px; height: 1023px; overflow: hidden; }
  body {
    background: var(--backdrop);
    font-family: "Open Sans", sans-serif;
    display: flex; align-items: center; justify-content: center;
  }
  .card {
    position: relative;
    width: 1000px; height: 572px;
    background: radial-gradient(ellipse at 45% 40%, var(--card-light) 0%, var(--card-mid) 70%, var(--card-edge) 100%);
    box-shadow: 0 10px 30px rgba(60,60,40,.18);
    overflow: hidden;
  }
  .icon-row {
    position: absolute; left: 64px; top: 56px;
    display: flex; gap: 22px;
  }
  .icon-tile { width: 150px; height: 150px; background: var(--tile); }
  .brand {
    position: absolute; left: 64px; top: 232px;
    font-size: 44px; font-weight: 400; letter-spacing: 17px;
    color: var(--ink);
  }
  .services {
    position: absolute; left: 64px; top: 296px;
    font-size: 21px; color: var(--ink); letter-spacing: .3px;
  }
  .services span + span { margin-left: 10px; }
  .person {
    position: absolute; left: 64px; top: 348px;
    font-size: 38px; font-weight: 700; letter-spacing: 3px; color: var(--ink-strong);
  }
  .person .role { font-weight: 600; letter-spacing: 1px; }
  .phone {
    position: absolute; left: 64px; top: 404px;
    display: flex; align-items: center; gap: 8px;
    font-size: 32px; color: var(--ink); letter-spacing: 2px;
  }
  .band {
    position: absolute; left: 0; right: 0; bottom: 0; height: 74px;
    background: var(--band);
    display: flex; align-items: center; justify-content: space-between;
    padding: 0 40px 0 34px;
    color: var(--band-text); font-weight: 700; font-size: 29px; letter-spacing: 1px;
  }
  .address { display: flex; align-items: center; gap: 14px; }
  .mini-icon { display: block; }
</style>
</head>
<body>
  <div class="card">
    <div class="icon-row">
      <div class="icon-tile" role="img" aria-label="Tractor icon for excavation"></div>
      <div class="icon-tile" role="img" aria-label="Pencil and drafting tools icon for custom designs"></div>
      <div class="icon-tile" role="img" aria-label="Vegetable icon for sustainable gardens"></div>
      <div class="icon-tile" role="img" aria-label="Flower icon for floriculture"></div>
    </div>

    <div class="brand">VERDANT HOLLOWS</div>
    <div class="services">
      <span>•Excavation</span><span>•Custom Property Designs</span><span>•Sustainable Gardens</span><span>•Floraculture</span>
    </div>

    <div class="person">HOWARD PELLIN/<span class="role">Contractor</span></div>
    <div class="phone">
      <svg class="mini-icon" width="22" height="22" viewBox="0 0 22 22" aria-hidden="true">
        <rect width="22" height="22" fill="#989c89"/>
        <path d="M7 5 l3 0 1 4 -2 1 q1 3 3 4 l1 -2 4 1 0 3 q-1 1 -3 1 q-8 -2 -8 -9 q0 -2 1 -3z" fill="#e8ecdc"/>
      </svg>
      <span>760-382-9174</span>
    </div>

    <div class="band">
      <div class="address">
        <svg class="mini-icon" width="24" height="24" viewBox="0 0 24 24" aria-hidden="true">
          <rect width="24" height="24" fill="#f2f3ec"/>
          <path d="M12 4 a5 5 0 0 1 5 5 c0 4 -5 10 -5 10 s-5 -6 -5 -10 a5 5 0 0 1 5 -5z" fill="#8b8f7d"/>
          <circle cx="12" cy="9" r="2" fill="#f2f3ec"/>
        </svg>
        <span>PO Box 208716 Carlsbad, CA 92013</span>
      </div>
      <div class="license">LIC C27-591046</div>
    </div>
  </div>
</body>
</html>
```